PDF flyer for our companies' two main products: Food processing machines.

PDF flyer with showcasing two products. Flyer can be one page per product, or both products on the same page.

Product #1: Labeled "Ribbon blenders".
Showing a photo of the machine, and the details/features offered with that machine. Product description must also say: "Sizes available; 2 Cu Ft. - 450 Cu Ft."

Product #2: Labeled: " Auger hoppers / Screw feeders"
Showing a photo of the machine, and the details/features offered with that machine.

SEE UPLOADED IMAGES; "Ribbon Blenders EXAMPLE FLYER".
& "Auger Hoppers / Screw Conveyors EXAMPLE FLYER" for a rough idea of what we are looking for.

Target Market(s)

Copackers, Packing houses, Food manufacturers, protein powder producers,

Industry/Entity Type

Commercial Food processing / packing / mixing equipment

Font styles to use
Serif

Colors
0054AA
0677BA
7BADD7
CADEEF
E8F1F8

Requirements
Must have
• Company logo on top of flyer.
Nice to have
• I would like for the flyer to show some stock images of common ingredients, similar to the images uploaded.
Should not have
• Pictures with background. Backgrounds must be removed from provides photos. "clipping path"

```html
<!DOCTYPE html>
<html lang="en">
<head>
<meta charset="utf-8">
<title>Ribbon Blenders &amp; Auger Hoppers – Hartwell Equipment</title>
<link href="https://fonts.googleapis.com/css2?family=Barlow+Condensed:wght@400;500;600;700&family=Poppins:wght@400;500;600&display=swap" rel="stylesheet">
<style>
  :root{
    --ink:#111111;
    --accent:#1aa3e6;
    --accent-deep:#0677BA;
    --cell:#dcedf8;
    --cell-alt:#eef6fb;
    --pale:#e8f1f8;
    --steel-1:#d9dcdf;
    --steel-2:#9ea4aa;
    --white:#ffffff;
  }
  *{box-sizing:border-box;margin:0;padding:0}
  html,body{width:1200px;height:675px;overflow:hidden;background:var(--white)}
  body{font-family:"Poppins",sans-serif;color:var(--ink)}
  .sheet{position:relative;width:1200px;height:675px;overflow:hidden;background:var(--white)}
  .abs{position:absolute}
  .heading{font-family:"Barlow Condensed",sans-serif;font-weight:700;line-height:1;color:var(--ink);letter-spacing:.2px}
  .subline{font-family:"Barlow Condensed",sans-serif;font-weight:500;font-size:17px;line-height:1;white-space:nowrap}
  .section-title{font-family:"Barlow Condensed",sans-serif;font-weight:600;font-size:17px;line-height:1;white-space:nowrap}
  .bullets{list-style:none}
  .bullets li{position:relative;font-size:8.4px;line-height:9.5px;padding-left:11px;margin-bottom:8px;letter-spacing:-.1px}
  .bullets li::before{content:"";position:absolute;left:1px;top:3.5px;width:3px;height:3px;border-radius:50%;background:var(--accent)}
  .divider{position:absolute;left:599.5px;width:1px;background:var(--ink)}
  .photo{position:absolute}

  /* brand */
  .brand{left:456px;top:27px;width:288px;height:82px;display:flex;align-items:center;justify-content:center;gap:10px}
  .brand-dot{width:14px;height:14px;border-radius:50%;background:var(--accent)}
  .brand-name{font-family:"Barlow Condensed",sans-serif;font-weight:700;font-size:30px;letter-spacing:1px;color:var(--ink);white-space:nowrap}

  /* spec tables */
  table{border-collapse:separate;border-spacing:1px;font-size:7px;white-space:nowrap}
  .blender-specs{left:36px;top:476px;width:523px}
  .blender-specs td{height:10.25px;padding:0 0 0 5px;line-height:10px;background:var(--cell-alt)}
  .blender-specs tr:nth-child(even) td{background:var(--cell)}
  .blender-specs tr td.label{background:var(--accent);color:var(--white);font-weight:500;width:78px}
  .blender-specs tr.head td{background:var(--ink);color:var(--white);font-weight:500}
  .blender-specs tr.head td.label{background:var(--accent)}
  .auger-specs{left:827px;top:400px;width:335px}
  .auger-specs td{height:16.5px;padding:0 0 0 6px;background:var(--cell)}
  .auger-specs tr td.label{background:var(--accent);color:var(--white);font-weight:500;width:73px}
  .auger-specs td.center{text-align:center;padding:0}
</style>
</head>
<body>
<div class="sheet">

  <div class="divider" style="top:0;height:17px"></div>
  <div class="divider" style="top:122px;height:522px"></div>

  <div class="abs brand">
    <span class="brand-dot"></span>
    <span class="brand-name">HARTWELL EQUIPMENT</span>
  </div>

  <!-- Ribbon blenders -->
  <h1 class="abs heading" style="left:37px;top:40px;font-size:32px">RIBBON BLENDERS</h1>
  <p class="abs subline" style="left:38px;top:74px">sizes offered: <span style="color:var(--accent)">2 Cu Ft - 450 Cu Ft.</span></p>

  <h2 class="abs section-title" style="left:38px;top:108px">STANDARD FEATURES:</h2>
  <ul class="abs bullets" style="left:38px;top:129px;width:262px">
    <li>304 stainless steel construction</li>
    <li>Pre-wired control panels with; batch timer, on/off switch, emergency stop button.</li>
    <li>Food grade compression shaft seals</li>
    <li>Safety sensor on lid for automatic shutoff when opened.</li>
    <li>Air actuated discharge value</li>
    <li>1 piece hinged lid with safety grating</li>
    <li>Power options; 220v/480v</li>
    <li>24” standard discharge height</li>
    <li>Castor wheels on 53cf units and smaller</li>
  </ul>

  <h2 class="abs section-title" style="left:38px;top:302px">OPTIONS:</h2>
  <ul class="abs bullets" style="left:38px;top:322px;width:250px">
    <li>Dual hinged lids available on custom orders</li>
    <li>Knife gate style discharge available on cutom orders</li>
    <li>Air purge seals available on custom orders</li>
    <li>316 stainless material available on custom orders</li>
    <li>Custom height modification</li>
    <li>Liquid spray systems</li>
    <li>(VFD) Variable Frequency Drives</li>
    <li>Leg extensions</li>
  </ul>

  <svg class="abs" style="left:261px;top:270px" width="19" height="60" viewBox="0 0 19 60"><polygon points="19,0 19,60 0,30" fill="var(--accent)"/></svg>

  <div class="photo" role="img" aria-label="Four wooden spoons holding ground spices" style="left:318px;top:152px;width:212px;height:52px;border-radius:26px;background:linear-gradient(90deg,#6f6a3e,#b8461f 35%,#9d8e6c 65%,#7c6b35)"></div>
  <div class="photo" role="img" aria-label="Stainless steel ribbon blender on castor legs with control panel" style="left:302px;top:212px;width:236px;height:250px;border-radius:6px;background:linear-gradient(135deg,var(--steel-1),var(--steel-2))"></div>

  <table class="abs blender-specs">
    <tr class="head"><td class="label">Model Size</td><td>5 CF</td><td>7 CF</td><td>10.5 CF</td><td>17.5 CF</td><td>35 CF</td><td>53 CF</td><td>70.5 CF</td><td>106 CF</td></tr>
    <tr><td class="label">Working Liters</td><td>120L</td><td>200L</td><td>300L</td><td>500L</td><td>1000L</td><td>1500L</td><td>2000L</td><td>3000L</td></tr>
    <tr><td class="label">Fill Capacity</td><td>5CF / 150L</td><td>9CF / 250L</td><td>13CF / 375L</td><td>22CF / 625L</td><td>44CF / 1250L</td><td>66CF / 1875L</td><td>88CF / 2500L</td><td>132CF / 3750L</td></tr>
    <tr><td class="label">Weight</td><td>440 lbs</td><td>550 lbs</td><td>770 lbs</td><td>1212 lbs</td><td>1874 lbs</td><td>2645 lbs</td><td>3527 lbs</td><td>5511 lbs</td></tr>
    <tr><td class="label">Motor Size</td><td>4hp</td><td>5.3hp</td><td>6.7hp</td><td>10hp</td><td>14.75hp</td><td>20hp</td><td>25hp</td><td>30hp</td></tr>
    <tr><td class="label">Total Length</td><td>50”</td><td>53.5”</td><td>63”</td><td>72”</td><td>94”</td><td>102”</td><td>131.5”</td><td>157.5”</td></tr>
    <tr><td class="label">Total Width</td><td>28”</td><td>34”</td><td>41.5”</td><td>45”</td><td>52”</td><td>66”</td><td>52.5”</td><td>54”</td></tr>
    <tr><td class="label">Total Height</td><td>66”</td><td>69”</td><td>71”</td><td>82”</td><td>87”</td><td>95”</td><td>76”</td><td>110”</td></tr>
    <tr><td class="label">Tub Length</td><td>31.5”</td><td>35.5”</td><td>41”</td><td>47”</td><td>59”</td><td>70”</td><td>75”</td><td>100”</td></tr>
    <tr><td class="label">Tub Width</td><td>16.5”</td><td>22”</td><td>25”</td><td>27.5”</td><td>35.5”</td><td>39”</td><td>48”</td><td>48”</td></tr>
    <tr><td class="label">Tub Height</td><td>20.5”</td><td>26”</td><td>28”</td><td>33”</td><td>41”</td><td>46”</td><td>51”</td><td>53”</td></tr>
    <tr><td class="label">Shaft Diameter</td><td>2”</td><td>2-1/4”</td><td>2-5/8”</td><td>3”</td><td>3.5”</td><td>4”</td><td>4”</td><td>5-1/4”</td></tr>
    <tr><td class="label">Tub Thickness</td><td>3mm</td><td>3mm</td><td>3mm</td><td>4mm</td><td>4mm</td><td>5mm</td><td>5mm</td><td>6mm</td></tr>
    <tr><td class="label">Ribbon Thickness</td><td>6mm</td><td>8mm</td><td>8mm</td><td>8mm</td><td>10mm</td><td>12mm</td><td>12mm</td><td>14mm</td></tr>
    <tr><td class="label">Max RPM</td><td>46 rpm</td><td>46 rpm</td><td>46 rpm</td><td>46 rpm</td><td>30 rpm</td><td>31 rpm</td><td>32 rpm</td><td>33 rpm</td></tr>
  </table>

  <!-- Auger hoppers -->
  <h1 class="abs heading" style="left:638px;top:181px;font-size:31px;line-height:31px">AUGER HOPPERS /<br>SCREW CONVEYORS</h1>
  <svg class="abs" style="left:904px;top:184px" width="18" height="56" viewBox="0 0 18 56"><polygon points="0,0 18,28 0,56" fill="var(--accent)"/></svg>

  <div class="photo" role="img" aria-label="Stainless steel auger hopper with inclined screw conveyor tube" style="left:930px;top:55px;width:222px;height:262px;border-radius:6px;background:linear-gradient(160deg,var(--steel-1),var(--steel-2))"></div>
  <div class="photo" role="img" aria-label="Pile of light grain flakes" style="left:624px;top:292px;width:128px;height:52px;border-radius:50% 50% 10% 10%;background:radial-gradient(ellipse at 50% 40%,#e2bf7e,#c8a266)"></div>
  <div class="photo" role="img" aria-label="Pile of dark seeds" style="left:772px;top:310px;width:104px;height:42px;border-radius:50% 50% 10% 10%;background:radial-gradient(ellipse at 50% 40%,#4b4a4a,#7a7876)"></div>
  <div class="photo" role="img" aria-label="Pile of brown powder" style="left:880px;top:298px;width:112px;height:48px;border-radius:50% 50% 10% 10%;background:radial-gradient(ellipse at 50% 40%,#b07a4c,#93623a)"></div>

  <h2 class="abs section-title" style="left:639px;top:402px">STANDARD FEATURES:</h2>
  <ul class="abs bullets" style="left:639px;top:424px;width:180px">
    <li>Direct Drive</li>
    <li>304 stainless steel construction</li>
    <li>Stainless steel safety grating</li>
    <li>Pre-wired control panel</li>
    <li>Electric Vibrator</li>
    <li>Castor wheels</li>
  </ul>

  <table class="abs auger-specs">
    <tr><td class="label">Model</td><td>AH-A2</td><td>AH-A3</td><td>AH-A5</td><td>AH-A7</td><td>AH-A8</td><td>AH-A12</td></tr>
    <tr><td class="label">Feeding Rate</td><td>2m³/Hr</td><td>3m³/Hr</td><td>5m³/Hr</td><td>7m³/Hr</td><td>8m³/Hr</td><td>12m³/Hr</td></tr>
    <tr><td class="label">Pipe Diameter</td><td>4”</td><td>4-1/2”</td><td>5-1/2”</td><td>6-1/4”</td><td>6-1/2”</td><td>8-1/2”</td></tr>
    <tr><td class="label">Hopper Vol.</td><td>3.5 CF</td><td class="center" colspan="5">7 CF</td></tr>
    <tr><td class="label">Dimensions</td><td>28.6” x 24.4” x 31.5”</td><td class="center" colspan="5">40” x 32” x 35”</td></tr>
    <tr><td class="label">Total Weight</td><td>221 LBS</td><td>287 LBS</td><td>397 LBS</td><td>441 LBS</td><td>485 LBS</td><td>596 LBS</td></tr>
    <tr><td class="label">Charging Height</td><td class="center" colspan="6">STANDARD 72 inches (40” - 196” available)</td></tr>
    <tr><td class="label">Charging Angle</td><td class="center" colspan="6">STANDARD 45˚ (30˚- 60˚ available)</td></tr>
  </table>

  <h2 class="abs section-title" style="left:639px;top:563px">OPTIONS:</h2>
  <ul class="abs bullets" style="left:639px;top:584px;width:270px">
    <li>Square or round hopper 3.5cf and 7cf hoppers are standard</li>
    <li>Custom hoppers up to 200cf</li>
    <li>VFD (Variable Frequency Drive)</li>
  </ul>
  <ul class="abs bullets" style="left:911px;top:584px;width:240px">
    <li>Clamshell Auger tube for easy cleanout</li>
    <li>316 Stainless steel construction</li>
  </ul>

</div>
</body>
</html>
```